Vira Nostalma is a dietary supplement company and in need of label design for 4 products

label for 4 dietary supplement products :1- Biotin. Red bottle ( please see the picture attached, not the whole bottle is colored but rather its a white bottle with the upper part and lower part of the bottle colored)2- COQ10. Orange Bottle 3- Hair Skin Nail. Pink bottle 4- Probiotics. Green Bottle we like the label to:1- have a modern and sleek appearance with very limited graphics.2- have a transparent background( as the bottle is white )3- have the box with the supplement and ingredient to appear sideways( horizontal )4- to have a color matching the bottle color.attached you will find :1- the dimension of the bottle.2- four different labels for each of the products.3- two pictures of the bottles 4- picture of the caps5- Logo
Industry/Entity Type
Health And Wellness
Colors
Designer to choose colors to be used in the design.
Look and feel
Each slider illustrates characteristics of the customer's brand and the style your logo design should communicate.

```html
<!DOCTYPE html>
<html lang="en">
<head>
<meta charset="utf-8">
<title>Vira Nostalma – Hair, Skin &amp; Nails Essentails Label</title>
<link href="https://fonts.googleapis.com/css2?family=Montserrat:wght@500;700;800&display=swap" rel="stylesheet">
<style>
  :root {
    --label-bg: #f3f3f4;
    --accent-pink: #e0249a;
    --frame-grey: #4a4a4c;
    --text-grey: #555557;
    --page-bg: #ffffff;
  }
  html, body {
    margin: 0;
    padding: 0;
    width: 1200px;
    height: 1200px;
    overflow: hidden;
    background: var(--page-bg);
  }
  .label {
    position: relative;
    width: 1200px;
    height: 1200px;
    background: var(--label-bg);
    font-family: "Montserrat", sans-serif;
  }
  .band {
    position: absolute;
    left: 0;
    width: 1200px;
    height: 22px;
    background: var(--accent-pink);
  }
  .band--top { top: 120px; }
  .band--bottom { top: 1080px; }

  .brand-box {
    position: absolute;
    left: 250px;
    top: 200px;
    width: 270px;
    height: 170px;
    border: 4px solid var(--frame-grey);
    box-sizing: border-box;
    display: flex;
    align-items: center;
    justify-content: center;
  }
  .brand-name {
    font-weight: 700;
    font-size: 34px;
    line-height: 1.1;
    color: var(--text-grey);
    text-align: center;
  }

  .product-title {
    position: absolute;
    left: 245px;
    top: 410px;
    margin: 0;
    font-weight: 800;
    font-size: 140px;
    line-height: 140px;
    letter-spacing: -2px;
    color: var(--accent-pink);
  }
  .product-sub {
    position: absolute;
    left: 250px;
    top: 840px;
    margin: 0;
    font-weight: 800;
    font-size: 72px;
    line-height: 72px;
    color: var(--text-grey);
  }
  .count {
    position: absolute;
    left: 250px;
    top: 1008px;
    font-weight: 800;
    font-size: 34px;
    line-height: 34px;
    color: var(--text-grey);
  }
  .frame-lines {
    position: absolute;
    left: 0;
    top: 0;
  }
</style>
</head>
<body>
  <div class="label">
    <div class="band band--top"></div>

    <div class="brand-box">
      <span class="brand-name">Vira<br>Nostalma</span>
    </div>

    <h1 class="product-title">HAIR,<br>SKIN &amp;<br>NAILS</h1>
    <p class="product-sub">ESSENTAILS</p>

    <svg class="frame-lines" width="1200" height="1200" viewBox="0 0 1200 1200" aria-hidden="true">
      <g fill="none" stroke="var(--frame-grey)" stroke-width="4">
        <polyline points="900,420 970,420 970,945 252,945 252,925"/>
        <polyline points="252,1005 252,985 970,985"/>
        <line x1="555" y1="1025" x2="970" y2="1025"/>
      </g>
    </svg>

    <span class="count">100 CAPSULES</span>

    <div class="band band--bottom"></div>
  </div>
</body>
</html>
```